Norwegian psychologist service needs a fresh and exiting web site*

Norwegian psychologist service: working with therapy, personal development, mastery and personal growth. Focus: children and teenagers with special needs; family dynamics; group processes; individuals with a need for therapy and personal growth. (Our company name: Fjordlys og samhold (means Mastery and Growth).

We already have a logo for the company, which will be used (will be attached in the project).

The webside is to be structured in 4 pages with roll down curtain menus (the numbers are just for guiding the designer - the should not be added):

Page 1: Om Fjordlys og Samhold (about Mastery and Growth): this is where our business is is presented/described shortly: Lorem Ipsum dolor cit...

Page 2: Tjenester (Services): this is where our 5 service areas are presented:
2.1 Utredning (Investigation, diagnosing): Lorem Ipsum dolor cit...
2.2 Rådgivning (consulting): Lorem Ipsum dolor cit...

2.3 Kurs og work shops (courses and work shops): Lorem Ipsum dolor cit...
2.3a Fjordlys og samhold Tema 1 (T1)
2.3b Fjordlys og samhold Tema 2 (T2)
2.3c Fjordlys og samhold Tema 3 (T3)

2.4 Terapi og utvikling (Therapy and development)
2.4a Fjordlys og samhold for individer (FS1)
2.4b Fjordlys og samhold i familier (FS2)
2.4c Fjordlys og samhold i grupper (FS3)
2.4d Fjordlys og samhold i institusjoner (FS4)

Page 3: Aktuelt (Blog): this is our blog where we share knowledge and articles

Page 4: Kontakt (Contact): This is the contact form page. Contact form should constitute:
- Ditt navn (your name)
- E-post (your e-mail)
- Emne (subject)
- Melding (message/description)

Our project should also include suggestion for handheld units (iPhone, iPad).
Updates

We have both been traveling with work for a while, and then unfortunately both of us got sick on return, so we need a few more days to evaluate and choose design. Kind Regards Arvid & Margit

Target Market(s)

Focus on therapy, learning, mastery and growth for children and teenagers with special needs, within the family dynamics, or in a group setting.
OUR MARKETS:
Private market: individuals, families, groups and health industry institutions (with focus on learning, mastery, growth (as well as growing up) and psychiatry for children and teenagers with special difficulties and needs)
Public institutions: Government institutions, state institutions and municipality institutions (e.g. schools, municipality health service, hospitals) that serve the public (families with children and teenagers with special needs, and where learning, mastery, growth (as well as growing up) and potential psychiatry is an issue).

Number of Pages Required

4 page

Font styles to use
Sans Serif

Colors

Designer to choose colors to be used in the design.

Requirements
Must have
• The website must have 4 pages with roll down curtain menus (we have added a PDF with suggested structure, and headings, with sub menus - see attached PDF drawing.
• The web page must also use the added logo file - and make the web page work well with our logo.
• We would like the website to have a modern look and we would like the site to be associated with typical HIGH END TOP QUALITY private health institutions, but with a stronger focus on human beings (hands, faces etc), and not white coats and doctors. We are psychologists in the private market.
• For instance, if photos are being used - we tend to like "warm" almost art-like, "grainy" two-tone (e.g. sepia) photos to illustrate our focus. If designer can find such photos as part of design, it would be interesting to us. We would like a few photos like that integrated in the design.
• We also want a design suggestion for how the web page should look like and behave on handheld units (e.g. iPhone, iPad).
Nice to have
• If designer could find a number of suitable photos that matches the business idea and design requirements (see description above), that could follow website, that would be good.
• It could also be nice to have graphic symbols that denote the different pages/subpages (subjects)....
• HORSES: we sometimes use horses as a "tool" in therapy sessions. The horse is not necessarily used for riding, but for contact, communication and grooming. PHOTOS: we would like the designer to find an opportunity for using a photo reflecting this cooperation between therapist, child, teenager and horse. It is a bit up to the designer to find a way to do this... Since the horse is only a tool, among many other tools, it does not have to be much - but we want to try and see how it will work with a photo that also reflects this part of our business.

```html
<!DOCTYPE html>
<html lang="en">
<head>
<meta charset="utf-8">
<title>Fjordlys og samhold</title>
<link rel="stylesheet" href="https://fonts.googleapis.com/css2?family=Poppins:wght@300;400;500;600&family=Lato:wght@400;700&display=swap">
<style>
:root{
  --ink:#1d1d1d;
  --text:#555;
  --muted:#7a7a7a;
  --navy:#2c3a9a;
  --navy-soft:#4a56a8;
  --green:#1f6b3b;
  --green-soft:#5c8a62;
  --hero:#121212;
  --light:#f5f5f4;
  --grey:#e7e7e6;
  --white:#fff;
  --footer:#151515;
  --sepia-a:#8c6a52;
  --sepia-b:#c9ad98;
}
*{box-sizing:border-box;margin:0;padding:0}
html,body{width:1200px;height:3550px;overflow:hidden}
body{font-family:'Poppins',sans-serif;color:var(--ink);background:var(--white);position:relative}
section,header,footer{position:absolute;left:0;width:1200px;overflow:hidden}
.abs{position:absolute}
.photo{position:absolute}
.eyebrow{font-size:13px;color:var(--navy);font-weight:400}
.h-section{font-weight:400;font-size:37px;line-height:1.1;color:var(--ink)}
.body-copy{font-family:'Lato',sans-serif;font-size:12.5px;line-height:19px;color:var(--text)}
.btn{position:absolute;display:flex;align-items:center;justify-content:center;gap:8px;font-size:11.5px;height:22px;border-radius:2px}
.btn-green{background:var(--green);color:#fff}
.btn-outline{border:1px solid #bbb;color:#444;background:#fff}
.arrow{display:inline-block;width:11px;height:1px;background:currentColor;position:relative}
.arrow:after{content:"";position:absolute;right:0;top:-2px;border-left:4px solid currentColor;border-top:2.5px solid transparent;border-bottom:2.5px solid transparent}

/* hero */
.hero{top:0;height:568px;background:radial-gradient(ellipse at 50% 40%,#222 0%,var(--hero) 70%)}
.hero-brand{left:124px;top:0;width:138px;height:134px;background:rgba(255,255,255,.03);border-radius:0 0 14px 14px;display:flex;align-items:flex-end;justify-content:center;padding-bottom:44px;color:rgba(255,255,255,.12);font-size:16px}
.hero-faint{left:188px;top:335px;width:840px;font-size:33px;font-weight:300;line-height:41px;color:rgba(255,255,255,.07)}
.hero-faint-btn{left:192px;top:448px;width:118px;height:20px;background:rgba(255,255,255,.04)}
.menu{left:0;top:150px;width:1200px;text-align:center;list-style:none;color:#e8e8e8}
.menu li{font-size:22px;font-weight:300;position:absolute;left:0;width:1200px}
.close{left:1064px;top:46px}

/* about */
.about{top:568px;height:486px;background:var(--light)}
.about .eyebrow{position:absolute;left:116px;top:86px}
.about h1{position:absolute;left:114px;top:112px;font-size:35px;font-weight:400;line-height:41px}
.about .lead{position:absolute;left:116px;top:212px;width:370px;font-size:12px;line-height:17px;color:#222;font-family:'Lato',sans-serif}
.about .body-copy{left:116px;top:262px;width:480px;position:absolute}
.img-back{left:774px;top:58px;width:309px;height:299px;background:linear-gradient(135deg,#6f4f3c,var(--sepia-b) 55%,#a98167)}
.img-front{left:690px;top:215px;width:230px;height:213px;background:linear-gradient(160deg,#ddd4cd,#6e625c);border:3px solid #fff}
.play{left:698px;top:66px}

/* services */
.services{top:1054px;height:622px;background:linear-gradient(180deg,#e4e4e3,#ececeb)}
.plant{left:110px;top:145px;width:186px;height:424px;background:linear-gradient(180deg,rgba(110,140,110,.35),rgba(170,185,170,.25));border-radius:40% 40% 12px 12px}
.services .eyebrow{position:absolute;left:362px;top:66px}
.services h2{position:absolute;left:361px;top:92px}
.services .sub{position:absolute;left:363px;top:136px;font-family:'Lato',sans-serif;font-size:12px;color:#333}
.card{position:absolute;background:#fff;text-align:center;display:flex;flex-direction:column;align-items:center;justify-content:center;padding:0 26px}
.card h3{font-size:13px;font-weight:500;color:#222;margin-top:10px}
.card p{font-family:'Lato',sans-serif;font-size:10.5px;line-height:17px;color:var(--muted);margin-top:10px}
.card .ico{width:44px;height:44px;border-radius:50%;background:#eceeea;display:flex;align-items:center;justify-content:center}
.card.active{background:var(--navy)}
.card.active h3,.card.active a{color:#fff}
.card.active .ico{background:#fff}
.card a{font-size:11px;text-decoration:underline;margin-top:14px;color:#fff}

/* team */
.team{top:1676px;height:662px;background:var(--light)}
.team h2{position:absolute;left:115px;top:68px}
.team .body-copy{position:absolute;left:116px;top:118px;width:448px;text-align:justify}
.team-img{left:627px;top:53px;width:456px;height:218px;background:linear-gradient(120deg,#e4dbd2,#a9907c 50%,#5d4a3e)}
.ref-img{left:116px;top:365px;width:474px;height:226px;background:linear-gradient(140deg,#7a604d,#c3ab96 50%,#5a4537)}
.ref-play{left:334px;top:454px}
.team .eyebrow2{position:absolute;left:621px;top:395px;font-size:10.5px;color:#333}
.team h3{position:absolute;left:620px;top:414px;font-weight:400;font-size:37px}
.team .ref-copy{position:absolute;left:621px;top:466px;width:446px;text-align:justify}
.team .ref-arrow{position:absolute;left:623px;top:558px;color:var(--navy)}

/* blog */
.blog{top:2338px;height:552px;background:#fafafa}
.blog h2{position:absolute;left:0;width:1200px;text-align:center;top:52px}
.blog .sub{position:absolute;left:0;width:1200px;text-align:center;top:118px;font-family:'Lato',sans-serif;font-size:12px;color:#333}
.post{position:absolute;top:169px;width:228px;height:260px;text-align:center}
.post .thumb{position:absolute;left:0;top:0;width:228px;height:133px}
.post .date{position:absolute;left:82px;top:94px;width:64px;height:64px;border-radius:50%;background:#fff;border:1px solid #e2e2e2;display:flex;flex-direction:column;align-items:center;justify-content:center;color:var(--green)}
.post .date b{font-size:20px;font-weight:500;line-height:20px}
.post .date span{font-size:9px;color:#333}
.post h3{position:absolute;top:176px;left:0;width:228px;font-size:13.5px;font-weight:500;color:#222}
.post p{position:absolute;top:205px;left:18px;width:192px;font-family:'Lato',sans-serif;font-size:10.5px;line-height:17px;color:var(--muted)}
.post .btn{top:262px;left:64px;width:100px}

/* cta */
.cta{top:2890px;height:373px;background:linear-gradient(90deg,#37428f,#4450a4 50%,#3a4592)}
.cta .scene{left:0;top:0;width:1200px;height:373px;background:radial-gradient(ellipse at 25% 60%,rgba(30,35,90,.45),transparent 40%),radial-gradient(ellipse at 75% 55%,rgba(30,35,90,.4),transparent 40%)}
.cta h2{position:absolute;left:0;width:1200px;top:134px;text-align:center;color:#f2f2f2;font-size:36px;font-weight:300;line-height:47px}
.cta .btn-white{left:471px;top:257px;width:118px;background:#fff;color:var(--navy);font-size:10.5px;font-weight:500}
.cta .link{position:absolute;left:607px;top:261px;font-size:11px;color:#e6e8f5}

/* footer */
.footer{top:3263px;height:287px;background:var(--footer);color:#d8d8d8}
.brand{left:116px;top:40px;display:flex;align-items:center;gap:8px;font-size:15px;color:#e9e9e9}
.brand i{display:block;width:14px;height:14px;border-radius:50%;background:#e9e9e9}
.footer .about-copy{position:absolute;left:116px;top:107px;width:476px;font-family:'Lato',sans-serif;font-size:11.5px;line-height:18px;color:#ddd}
.footer h4{position:absolute;top:42px;font-size:14px;font-weight:400;color:#eee}
.links{position:absolute;left:645px;top:76px;list-style:none;font-size:11px;line-height:23px}
.links li:before{content:"›";color:var(--green-soft);margin-right:10px}
.contact{position:absolute;left:856px;top:76px;list-style:none;font-size:11px;line-height:18px}
.contact li{display:flex;gap:10px;margin-bottom:8px}
.contact svg{flex:none;margin-top:3px}
.bar{position:absolute;left:0;top:237px;width:1200px;height:50px;background:var(--navy);display:flex;align-items:center;padding:0 116px;font-size:9.5px;color:#c6cbea}
.bar .soc{margin-left:auto;display:flex;gap:8px}
.bar .soc i{display:block;width:7px;height:7px;border-radius:50%;background:#c6cbea}
</style>
</head>
<body>

<header class="hero">
  <div class="abs hero-brand">Fjordlys</div>
  <p class="abs hero-faint">We are working with therapy, personal development, mastery and personal growth</p>
  <div class="abs hero-faint-btn"></div>
  <svg class="abs close" width="22" height="22" viewBox="0 0 22 22" aria-label="Close menu"><path d="M4 4L18 18M18 4L4 18" stroke="#fff" stroke-width="4" stroke-linecap="round"/></svg>
  <nav>
    <svg class="abs" style="left:586px;top:158px" width="28" height="28" viewBox="0 0 28 28" aria-label="Home"><path d="M4 13L14 4l10 9M7 11v13h5v-7h4v7h5V11" fill="none" stroke="#eee" stroke-width="1.6" stroke-linejoin="round"/></svg>
    <ul class="menu abs">
      <li style="top:66px">About Fjordlys og samhold</li>
      <li style="top:121px">Services</li>
      <li style="top:169px">Blog</li>
      <li style="top:222px">Contact us</li>
    </ul>
  </nav>
</header>

<section class="about">
  <p class="eyebrow">About us</p>
  <h1>Professional<br>Psychology Therapy</h1>
  <p class="lead">Curabitur eu erat sit amet sapien pharetra maximus. Orci varius natoque penatibus et magnis dis parturient montes,</p>
  <p class="body-copy">Lorem ipsum dolor sit amet, consectetur adipiscing elit. Suspendisse eget enim ultricies, sodales odio ornare, ultrices dui. Nulla neque massa, gravida sollicitudin volutpat quis, pellentesque in sem. Ut et gravida risus. Aliquam diam diam, dignissim at porta sit amet, dignissim eget nisl. Vestibulum luctus laoreet libero.</p>
  <a class="btn btn-green" style="left:116px;top:362px;width:120px">Contact Us <span class="arrow"></span></a>
  <div class="photo img-back" role="img" aria-label="Sepia photo of two hands clasped together"></div>
  <div class="photo img-front" role="img" aria-label="Sepia photo of a mother and child laughing together"></div>
  <svg class="abs play" width="116" height="116" viewBox="0 0 116 116" aria-label="Play video"><circle cx="58" cy="58" r="57" fill="#8e97cf" opacity=".75"/><circle cx="58" cy="58" r="47" fill="var(--navy)"/><path d="M49 40v36l30-18z" fill="#fff"/></svg>
</section>

<section class="services">
  <div class="photo plant" role="img" aria-label="Eucalyptus branches in a glass vase"></div>
  <p class="eyebrow">My Services</p>
  <h2 class="h-section">Our Services</h2>
  <p class="sub">Sed ut perspiciatis unde omnis iste natus error sit voluptatem accusantiumdoloremque laudantium, totam rem aperiam,</p>

  <div class="card" style="left:362px;top:196px;width:228px;height:379px">
    <div class="ico"><svg width="22" height="22" viewBox="0 0 22 22"><path d="M6 19l2-8 5-6 3 2-1 3 2 3-3 1-3-1-1 6z" fill="var(--green-soft)"/></svg></div>
    <h3>Equine Therapy</h3>
    <p>Sed ut perspiciatis unde omnis iste natus error sit voluptatem accusantium doloremque laudantium, totam rem aperiam, eaque ipsa quae ab illo inventore veritatis et quasi architecto beatae vitae dicta sunt explicabo.</p>
  </div>
  <div class="card active" style="left:609px;top:196px;width:227px;height:179px">
    <div class="ico"><svg width="22" height="22" viewBox="0 0 22 22"><path d="M3 11c3-5 13-5 16 0-3 5-13 5-16 0z" fill="none" stroke="var(--green-soft)" stroke-width="1.6"/><circle cx="11" cy="11" r="2.6" fill="var(--green-soft)"/></svg></div>
    <h3>Investigation, diagnosing</h3>
    <a>Read More</a>
  </div>
  <div class="card" style="left:856px;top:196px;width:227px;height:179px">
    <div class="ico"><svg width="22" height="22" viewBox="0 0 22 22"><circle cx="11" cy="8" r="4" fill="var(--green-soft)"/><path d="M4 20c0-5 3-7 7-7s7 2 7 7z" fill="var(--green-soft)"/></svg></div>
    <h3>Consulting</h3>
    <p>Lorem ipsum dolor sit amet, consectetur adipiscing elit</p>
  </div>
  <div class="card" style="left:609px;top:396px;width:227px;height:179px">
    <div class="ico"><svg width="22" height="22" viewBox="0 0 22 22"><rect x="5" y="3" width="12" height="16" rx="1.5" fill="var(--green-soft)"/><path d="M8 7h6M8 10h6" stroke="#fff" stroke-width="1.2"/></svg></div>
    <h3>Courses and work shops</h3>
    <p>Lorem ipsum dolor sit amet, consectetur adipiscing elit</p>
  </div>
  <div class="card" style="left:856px;top:396px;width:227px;height:179px">
    <div class="ico"><svg width="22" height="22" viewBox="0 0 22 22"><path d="M3 6l5 4v8L3 14zM19 6l-5 4v8l5-4z" fill="var(--green-soft)"/></svg></div>
    <h3>Therapy and development</h3>
    <p>Lorem ipsum dolor sit amet, consectetur adipiscing elit</p>
  </div>
</section>

<section class="team">
  <h2 class="h-section">Highly Qualified Team</h2>
  <p class="body-copy">Lorem ipsum dolor sit amet, consectetur adipiscing elit. Maecenas vehicula magna eget lectus feugiat cursus. Vestibulum vestibulum aliquam justo lacinia volutpat. Praesent eu pharetra mauris, aliquet rhoncus ipsum. Sed arcu nisl, aliquam at cursus vitae, placerat eget purus. In quis consequat sapien, non ultrices tortor.</p>
  <a class="btn btn-green" style="left:116px;top:216px;width:120px">Contact Us <span class="arrow"></span></a>
  <div class="photo team-img" role="img" aria-label="Sepia photo of a team gathered around laptops in an office"></div>

  <div class="photo ref-img" role="img" aria-label="Sepia photo of many hands meeting in a circle on the ground"></div>
  <svg class="abs ref-play" width="38" height="38" viewBox="0 0 38 38" aria-label="Play video"><circle cx="19" cy="19" r="18" fill="#fff" opacity=".85"/><path d="M15 12v14l11-7z" fill="#555"/></svg>
  <p class="eyebrow2">RECOMENDATIONS</p>
  <h3>We have great references.</h3>
  <p class="body-copy ref-copy">Lorem ipsum dolor sit amet, consectetur adipiscing elit. Maecenas vehicula magna eget lectus feugiat cursus. Vestibulum vestibulum aliquam justo lacinia volutpat. Praesent eu pharetra mauris, aliquet rhoncus ipsum. Sed arcu nisl, aliquam at cursus vitae, placerat eget purus. In quis consequat sapien, non ultrices tortor.</p>
  <span class="ref-arrow arrow"></span>
</section>

<section class="blog">
  <h2 class="h-section">Our Blogs</h2>
  <p class="sub">Lorem ipsum dolor sit amet, consectetur adipiscing elit. Maecenas vehicula magna eget lectus feugiat cursus.</p>

  <article class="post" style="left:116px">
    <div class="thumb" role="img" aria-label="Sepia photo of a parent holding a small child's hand" style="background:linear-gradient(135deg,#e7d6cb,#a67f6c)"></div>
    <div class="date"><b>12</b><span>FEB</span></div>
    <h3>Psychology Therapy</h3>
    <p>Lorem ipsum dolor sit amet, consectetur adipiscing elit</p>
    <a class="btn btn-green" style="top:262px;left:64px;width:96px">Read More <span class="arrow"></span></a>
  </article>
  <article class="post" style="left:362px">
    <div class="thumb" role="img" aria-label="Sepia portrait of a smiling young woman" style="background:linear-gradient(135deg,#6a4c3c,#c8a994 60%,#8b6a57)"></div>
    <div class="date"><b>09</b><span>FEB</span></div>
    <h3>Restoring Confidence</h3>
    <p>Lorem ipsum dolor sit amet, consectetur adipiscing elit</p>
    <a class="btn btn-outline">Read More <span class="arrow"></span></a>
  </article>
  <article class="post" style="left:609px">
    <div class="thumb" role="img" aria-label="Sepia photo of a young seedling growing from soil" style="background:linear-gradient(180deg,#b79d89,#5f4536)"></div>
    <div class="date"><b>21</b><span>JAN</span></div>
    <h3>Work Improvements</h3>
    <p>Lorem ipsum dolor sit amet, consectetur adipiscing elit</p>
    <a class="btn btn-outline">Read More <span class="arrow"></span></a>
  </article>
  <article class="post" style="left:856px">
    <div class="thumb" role="img" aria-label="Sepia photo of a horse and a person in a forest" style="background:linear-gradient(135deg,#7a5f4f,#b49885 50%,#6c5344)"></div>
    <div class="date"><b>12</b><span>JAN</span></div>
    <h3>EquineTherapy</h3>
    <p>Lorem ipsum dolor sit amet, consectetur adipiscing elit</p>
    <a class="btn btn-outline">Read More <span class="arrow"></span></a>
  </article>
</section>

<section class="cta">
  <div class="photo scene" role="img" aria-label="Blue-toned photo of two women talking across a table"></div>
  <h2>Friendly atmosphere<br>for all of your thoughts</h2>
  <a class="btn btn-white">Schedule a visit <span class="arrow"></span></a>
  <span class="link">Find out more About us</span>
</section>

<footer class="footer">
  <div class="abs brand"><i></i>Fjordlys og samhold</div>
  <p class="about-copy">Lorem ipsum dolor sit amet, consectetur adipiscing elit. Maecenas vehicula magna eget lectus feugiat cursus. Vestibulum vestibulum aliquam justo lacinia volutpat. Praesent eu pharetra mauris, aliquet rhoncus ipsum. Sed arcu nisl, aliquam at cursus vitae, placerat eget purus. In quis consequat sapien, non ultrices tortor.</p>
  <h4 style="left:645px">Quick links</h4>
  <ul class="links">
    <li>About Fjordlys og samhold</li>
    <li>Our Services</li>
    <li>Blog</li>
    <li>Contact</li>
    <li>Privacy Policy</li>
  </ul>
  <h4 style="left:856px">Contact Address</h4>
  <ul class="contact">
    <li><svg width="9" height="11" viewBox="0 0 9 11"><path d="M4.5 0a4 4 0 0 1 4 4c0 3-4 7-4 7S.5 7 .5 4a4 4 0 0 1 4-4z" fill="var(--green-soft)"/><circle cx="4.5" cy="4" r="1.4" fill="#151515"/></svg><span>14 Bryggegata, 5003 Bergen<br>Vestland Norge</span></li>
    <li><svg width="10" height="10" viewBox="0 0 10 10"><path d="M2 0l2 2.5-1 1.3c.7 1.4 1.8 2.5 3.2 3.2l1.3-1L10 8l-1.5 2C4 10 0 6 0 1.5z" fill="var(--green-soft)"/></svg><span>(47) 555 -0142 -000</span></li>
    <li><svg width="11" height="9" viewBox="0 0 11 9"><rect width="11" height="9" rx="1" fill="var(--green-soft)"/><path d="M0 1l5.5 4L11 1" stroke="#151515" fill="none"/></svg><span>post@fjordlys-samhold.no</span></li>
  </ul>
  <div class="bar">Copyright © Fjordlys— All Rights Reserve<div class="soc"><i></i><i></i></div></div>
</footer>

</body>
</html>
```